Patient "menu"/catalog for IV Therapy spa

We have a "menu" that's basically just a bunch of Word documents explaining what we do and what's in each package, but it's weak. We had the pages laminated and bound at Paper Harbor and they look like crap. I also need to add information and be able to edit the pages. We HAVE to print the "catalog" with Printowl and want the size to be 5.5"x8.5" and glossy. We're imagining our logo on the front page, some "what to expect" and "what we're all about" info on the inside cover, and then each IV package and injection will have its own page. We can start with the copy that's currently on our menu, but we need to add some things to several of the pages. Things change all the time in this industry, and we're expanding regularly, so we have to have the ability to alter and reprint. I'm attaching some of the current files.

Target Market(s)

Current patients

Industry/Entity Type

Medical

Font styles to use
Other font styles liked:
• Whatever is on our bifold brochure would be fine.

Colors
0094D4
00A9DD
6FCCEA
C7EBF8
E9F6FB
00AB8E
00BBA5
67D7C9
C6EFE9
E9F9F6

Requirements
Must have
• 5.5:x8.5", printable at Printowl. Must be two-sided and editable by us for future changes
Nice to have
• Gotta be glossy and cool, but professional.
Should not have
• Stock images that we don't provide

```html
<!DOCTYPE html>
<html lang="en">
<head>
<meta charset="utf-8">
<title>IV Therapy Menu – Migraine Relief &amp; The Essential</title>
<link rel="stylesheet" href="https://fonts.googleapis.com/css2?family=Roboto:wght@400;700&family=Saira+Condensed:wght@400;500;600&display=swap">
<style>
  :root {
    --blue-deep: #0094D4;
    --blue: #00A9DD;
    --blue-mid: #6FCCEA;
    --blue-soft: #C7EBF8;
    --blue-mist: #E9F6FB;
    --teal-deep: #00AB8E;
    --teal: #00BBA5;
    --teal-mid: #67D7C9;
    --teal-soft: #C6EFE9;
    --teal-mist: #E9F9F6;
    --ink: #1d1d1f;
    --body: #3a3a3c;
    --paper: #ffffff;
    --stage: #eef0f2;
  }
  * { box-sizing: border-box; margin: 0; padding: 0; }
  html, body { width: 1200px; height: 900px; overflow: hidden; background: var(--stage); }
  body { font-family: "Roboto", Arial, sans-serif; color: var(--body); }

  .spread {
    position: absolute; left: 50px; top: 25px;
    width: 1100px; height: 850px;
    display: flex;
    box-shadow: 0 6px 24px rgba(0,0,0,.12);
  }
  .page {
    position: relative; width: 550px; height: 850px;
    background: var(--paper); overflow: hidden;
  }
  .page--left { border-right: 1px solid #e3e6e8; }

  .page__rule { position: absolute; top: 0; left: 0; right: 0; height: 5px; background: var(--teal); }

  .page__title {
    position: absolute; top: 26px; right: 36px; z-index: 3;
    font-family: "Saira Condensed", "Arial Narrow", sans-serif;
    font-weight: 500; font-size: 46px; line-height: 1; color: var(--ink);
  }
  .page__title .accent { color: var(--teal); }

  .hero-bg { position: absolute; left: 0; top: 0; width: 550px; height: 380px; }

  .hero-photo {
    position: absolute; z-index: 1;
  }
  .hero-photo--portrait {
    right: 60px; top: 105px; width: 170px; height: 200px;
    background: linear-gradient(180deg, #f1f3f5, #d9dde2);
    border-radius: 6px;
  }
  .hero-photo--landscape {
    left: 0; top: 0; width: 550px; height: 330px;
    background: linear-gradient(135deg, #7fb6d8 0%, #3f9a3a 35%, #2f8a2c 60%, #a9cf3a 100%);
  }

  .page-num {
    position: absolute; z-index: 4; right: 30px;
    width: 28px; height: 28px; border-radius: 50%;
    background: var(--blue-soft); color: var(--ink);
    font-size: 11px; font-weight: 700;
    display: flex; align-items: center; justify-content: center;
  }

  .content { position: absolute; left: 40px; right: 40px; z-index: 2; font-size: 11.5px; line-height: 1.45; }
  .lead { font-weight: 700; color: var(--ink); margin-bottom: 10px; }
  .intro { margin-bottom: 16px; }
  .contains-title {
    font-family: "Saira Condensed", "Arial Narrow", sans-serif;
    font-size: 20px; font-weight: 500; color: var(--teal); margin-bottom: 6px;
  }
  .ingredients { list-style: none; }
  .ingredients li { margin-bottom: 3px; }
  .ingredients b { color: var(--ink); }
  .price {
    display: inline-block; margin-top: 18px;
    padding: 6px 16px;
    background: var(--teal-soft); color: var(--teal);
    font-family: "Saira Condensed", "Arial Narrow", sans-serif;
    font-size: 28px; font-weight: 500;
  }

  .ring {
    position: absolute; right: -40px; bottom: 110px;
    width: 150px; height: 150px; border-radius: 50%;
    border: 16px solid var(--teal-mist);
  }

  .footer-band { position: absolute; left: 0; right: 0; bottom: 40px; height: 70px; }
  .footer-band__line {
    position: absolute; left: 0; right: 0; top: 32px; height: 8px;
    background: linear-gradient(90deg, var(--blue), var(--teal));
  }
  .footer-band__pill {
    position: absolute; left: 30px; top: 0; width: 330px; height: 70px;
    border-radius: 18px;
    background: linear-gradient(90deg, var(--blue-deep), var(--teal));
    color: #fff; font-family: "Saira Condensed", "Arial Narrow", sans-serif;
    font-size: 24px; letter-spacing: .5px;
    display: flex; align-items: center; justify-content: center;
  }
</style>
</head>
<body>
<main class="spread">

  <!-- Page 07 -->
  <section class="page page--left">
    <svg class="hero-bg" viewBox="0 0 550 380" aria-hidden="true">
      <defs>
        <linearGradient id="mist" x1="0" y1="0" x2="1" y2="1">
          <stop offset="0" stop-color="#E9F6FB"/>
          <stop offset="1" stop-color="#f6fafc"/>
        </linearGradient>
      </defs>
      <path d="M0 0 H550 V380 C420 260 200 210 0 250 Z" fill="url(#mist)"/>
      <path d="M0 250 C200 210 420 260 550 380 L550 370 C420 250 200 195 0 232 Z" fill="#C7EBF8"/>
    </svg>
    <div class="page__rule"></div>
    <h1 class="page__title"><span class="accent">Migraine</span> Relief</h1>
    <div class="hero-photo hero-photo--portrait" role="img" aria-label="Photo of a person holding their head with a headache"></div>
    <div class="page-num" style="top:318px">07</div>

    <div class="content" style="top:340px">
      <p class="lead">Sometimes you don't need all the fluids and meds, and just a little boost will do. That's why we offer select injections.</p>
      <p class="intro">One full liter of Ringer's Lactate infused with muscle-relaxing magnesium, a pile of B complex, pain reliever, nausea meds, and medical oxygen.</p>
      <h2 class="contains-title">Contains</h2>
      <ul class="ingredients">
        <li><b>Ringer's Lactate</b> 1L (Potassium Chloride 0.3 g/L, Sodium Chloride 6 g/L, Sodium Lactate 3.1 g/L, Calcium chloride 0.2 g/L)</li>
        <li><b>Magnesium</b> (a natural muscle relaxant) 1g</li>
        <li><b>Folic Acid</b> (a B complex vitamin) 1mg</li>
        <li><b>Thiamine</b> (a B complex vitamin) 100mg</li>
        <li><b>Ondansetron</b> (generic Emeza for nausea) 4mg</li>
        <li><b>Ketorolac</b> (generic Painora for pain/headache) 30mg</li>
        <li><b>Medical oxygen</b> 30 minutes @ 2LPM to dilate your blood vessels</li>
      </ul>
      <div class="price">$149</div>
    </div>

    <div class="ring" aria-hidden="true"></div>
    <div class="footer-band">
      <div class="footer-band__line"></div>
      <div class="footer-band__pill">www.calmcurrentclinic.com</div>
    </div>
  </section>

  <!-- Page 08 -->
  <section class="page page--right">
    <div class="hero-photo hero-photo--landscape" role="img" aria-label="Photo of a waterfall surrounded by lush green forest"></div>
    <svg class="hero-bg" viewBox="0 0 550 380" aria-hidden="true" style="z-index:2">
      <path d="M0 250 C200 210 420 260 550 380 L550 380 L0 380 Z" fill="#ffffff"/>
      <path d="M0 250 C200 210 420 260 550 380 L550 366 C420 246 200 196 0 236 Z" fill="#C7EBF8" opacity=".9"/>
    </svg>
    <div class="page__rule" style="z-index:3"></div>
    <h1 class="page__title"><span class="accent">The</span> Essential</h1>
    <div class="page-num" style="top:318px">08</div>

    <div class="content" style="top:340px">
      <p class="lead">Perfect for when you really need fluids without all the vitamins, minerals, bells and whistles.</p>
      <p class="intro">One full liter of balanced fluid, Ringer's Lactate. Ringer's is closer to your blood's actual chemistry than Normal Saline (which is just salt water), so it's all we use.</p>
      <h2 class="contains-title">Contains</h2>
      <ul class="ingredients">
        <li><b>Sterile water</b> 1L</li>
        <li><b>Potassium Chloride</b> 0.3 g/L</li>
        <li><b>Sodium Chloride</b> 6 g/L</li>
        <li><b>Sodium Lactate</b> 3.1 g/L</li>
        <li><b>Calcium chloride</b> 0.2 g/L</li>
        <li>Lactated Ringer's contains ions of <b>sodium</b> 130 mEq/L, <b>potassium</b> 4 mEq/L, <b>calcium</b> 2.7 mEq/L, <b>chloride</b> 109 mEq/L and lactate 28 mEq/L.</li>
      </ul>
      <div class="price">$99</div>
    </div>

    <div class="ring" aria-hidden="true"></div>
    <div class="footer-band">
      <div class="footer-band__line"></div>
      <div class="footer-band__pill">www.calmcurrentclinic.com</div>
    </div>
  </section>

</main>
</body>
</html>
```